Corrigan's Irish Pub Menu Design

New menu design for Corrigan's Irish Pub prefer someone with menu design experience. Menu items are attached and I'll need working files to make updates. The design should be 8.5"x14" 1 cover page and 3 page menu if possible or 4 page menu if not with a Header on the first page this is for print and web. Please include the new logo and it should be in a traditional Irish Pub style. When complete please send a proof for markup (watermark is fine just want to markup and proof) and I'll send back for revisions.
Colors
Designer to choose colors to be used in the design.
Look and feel
Each slider illustrates characteristics of the customer's brand and the style your logo design should communicate.

```html
<!DOCTYPE html>
<html lang="en">
<head>
<meta charset="utf-8">
<title>Corrigan's Irish Pub — Wraps, Flat Breads &amp; Entrees</title>
<link href="https://fonts.googleapis.com/css2?family=Marcellus&family=Josefin+Sans:wght@300;400;600&display=swap" rel="stylesheet">
<style>
  :root{
    --ink:#1d3a2f;
    --ink-soft:#2b4a3e;
    --backdrop:#e6e6e6;
    --paper-a:#eef0f1;
    --paper-b:#d9dadc;
    --leaf-a:#3f6b2a;
    --leaf-b:#c9b48a;
    --bread-a:#c9a46a;
    --bread-b:#efe7b4;
  }
  *{margin:0;padding:0;box-sizing:border-box}
  html,body{width:1200px;height:1200px;overflow:hidden;background:var(--backdrop)}
  .spread{position:absolute;left:30px;top:132px;width:1140px;height:936px;display:flex}
  .page{position:relative;width:570px;height:936px;display:flex}
  .photo{width:170px;height:100%}
  .photo--wrap{background:linear-gradient(160deg,var(--leaf-a) 0%,#8ea760 30%,var(--leaf-b) 55%,#5f8a3a 80%,#9bbf6a 100%)}
  .photo--salad{width:168px;background:linear-gradient(175deg,var(--bread-a) 0%,#b88a55 22%,var(--bread-b) 40%,#6b8f45 62%,#f3df7a 78%,#e9e5d8 100%)}
  .rule{width:5px;height:100%;background:var(--ink)}
  .panel{position:relative;flex:1;background:linear-gradient(100deg,var(--paper-a),var(--paper-b));color:var(--ink)}
  .page--right .panel{background:linear-gradient(100deg,var(--paper-b) 0%,var(--paper-a) 30%,var(--paper-b) 100%)}
  .abs{position:absolute}
  .section-title{font-family:"Marcellus",serif;color:var(--ink);left:0;right:0;text-align:center;white-space:nowrap}
  .section-title--big{font-size:50px;letter-spacing:2px}
  .section-title--mid{font-size:23px}
  .section-note{font-family:"Josefin Sans",sans-serif;font-size:12px;left:0;right:0;text-align:center}
  .item-name{font-family:"Marcellus",serif;font-size:23px;white-space:nowrap}
  .item-name .the{font-size:19px}
  .item-name::after{content:"";position:absolute;left:0;top:34px;width:82px;height:3px;background:var(--ink)}
  .price{font-family:"Marcellus",serif;font-size:22px;white-space:nowrap}
  .price small{font-size:17px;margin-left:4px}
  .desc{font-family:"Josefin Sans",sans-serif;font-weight:600;font-size:11.5px;line-height:16px;letter-spacing:.3px;color:var(--ink-soft)}
  .entree{font-family:"Josefin Sans",sans-serif;font-weight:300;font-size:16px;letter-spacing:.6px;display:flex;align-items:baseline;left:30px;width:331px}
  .entree .dots{flex:1;border-bottom:1.5px dotted var(--ink);margin:0 4px;transform:translateY(-3px)}
  .entree .amp{font-size:14px}
  .entree-desc{font-family:"Josefin Sans",sans-serif;font-weight:300;font-size:11px;line-height:16px;letter-spacing:.8px;left:30px;width:310px}
</style>
</head>
<body>
<main class="spread">
  <section class="page page--left">
    <div class="photo photo--wrap" role="img" aria-label="Close-up photo of a grilled wrap with jalapeños, lettuce and bacon"></div>
    <div class="rule"></div>
    <div class="panel">
      <h1 class="abs section-title section-title--big" style="top:120px">WRAPS</h1>

      <h2 class="abs item-name" style="left:30px;top:218px"><span class="the">the</span> CHICKEN WRAP</h2>
      <span class="abs price" style="left:315px;top:220px">12</span>
      <p class="abs desc" style="left:30px;top:276px">Grilled or Blackend Chicken, Lettuce, Tomato,<br>Red Onion, Applewood Bacon and a Parmesan Ranch</p>

      <h2 class="abs item-name" style="left:30px;top:336px"><span class="the">the</span> TURKEY WRAP</h2>
      <span class="abs price" style="left:315px;top:338px">12</span>
      <p class="abs desc" style="left:30px;top:394px">Smoked Turkey, Swiss Cheese, Spinach, Tomato,<br>Applewood Bacon, Candled Whiskey Walnuts,<br>Cranberry Aioli</p>

      <h2 class="abs item-name" style="left:30px;top:470px"><span class="the">the</span> HADDOCK WRAP</h2>
      <span class="abs price" style="left:315px;top:472px">13</span>
      <p class="abs desc" style="left:30px;top:528px">Grilled or Blackend Haddock, Lettuce, Tomato,<br>Cheddar Cheese and Remoulade</p>

      <h2 class="abs item-name" style="left:30px;top:589px"><span class="the">the</span> SALMON WRAP</h2>
      <span class="abs price" style="left:315px;top:592px">13</span>
      <p class="abs desc" style="left:30px;top:646px">Grilled or Blackend Haddock, Spinach, Tomato,<br>Scallions, Gouda Cheese, and Garlic and Thyme Aioli</p>

      <h2 class="abs item-name" style="left:30px;top:707px"><span class="the">the</span> VEGGIE WRAP</h2>
      <span class="abs price" style="left:315px;top:710px">12<small>v</small></span>
      <p class="abs desc" style="left:30px;top:765px">Artichokes, Spinach, Tomato, Cucumbers,<br>Red Onion, Mozz Cheese and a Roasted Red Pepper Aioli</p>
    </div>
  </section>

  <section class="page page--right">
    <div class="photo photo--salad" role="img" aria-label="Close-up photo of a plated salad with toast, shredded cheese, greens and a halved boiled egg"></div>
    <div class="rule"></div>
    <div class="panel">
      <h1 class="abs section-title section-title--mid" style="top:42px">10″ FLAT BREADS</h1>
      <p class="abs section-note" style="top:82px">With a Gluten Free Cauliflour Crust</p>

      <h2 class="abs item-name" style="left:30px;top:122px">BBQ PORK</h2>
      <span class="abs price" style="left:314px;top:124px">12<small>gf</small></span>
      <p class="abs desc" style="left:30px;top:179px">Corrigan's BBQ Sauce, Pulled Mojo Pork, Sliced Apples,<br>Blue Cheese Crumbles and Mozz Cheese</p>

      <h2 class="abs item-name" style="left:30px;top:240px">BUFFALO CHICKEN</h2>
      <span class="abs price" style="left:314px;top:242px">12</span>
      <p class="abs desc" style="left:30px;top:297px">Blackwater Buffalo Sauce, Pulled Chicken, Diced Celery,<br>Scallions, Blue Cheese, Crumbles and Mozz Cheese</p>

      <h2 class="abs item-name" style="left:30px;top:374px">IRISH BANGER</h2>
      <span class="abs price" style="left:314px;top:376px">12</span>
      <p class="abs desc" style="left:30px;top:431px">Stout Grain Mustard Sauce, Bangers, Applewood Bacon,<br>Onions, Roasted Red Pepper and Smoked Gouda Cheese</p>

      <h2 class="abs item-name" style="left:30px;top:493px">VEGGIE PIE</h2>
      <span class="abs price" style="left:314px;top:496px">12<small>gf</small></span>
      <p class="abs desc" style="left:30px;top:549px">Whiskeyed Fig Cream Cheese Sauce, Spinach, Artichokes,<br>Cherry Tomatoes, Cucumber, Scallions, Parmesan<br>and Smoked Gouda Cheese</p>

      <h1 class="abs section-title section-title--mid" style="top:639px">ENTREE’S</h1>

      <p class="abs entree" style="top:677px">BANGERS AND MASH<span class="dots"></span>15</p>
      <p class="abs entree" style="top:710px">SHEPHERD’S PIE<span class="dots"></span>13</p>
      <p class="abs entree" style="top:743px">FISH AND CHIPS<span class="dots"></span>13</p>
      <p class="abs entree" style="top:777px">CORNED BEEF <span class="amp">&nbsp;and&nbsp;</span> CABBAGE<span class="dots"></span>13</p>
      <p class="abs entree-desc" style="top:799px">Blackwater Pulled Corned Beef with Caraway Cabbage<br>and Smoked Goud Mashed Potatoes. Served with<br>Stout Mustard</p>
      <p class="abs entree" style="top:857px">GARLIC BREAKFAST PLATE<span class="dots"></span>12</p>
    </div>
  </section>
</main>
</body>
</html>
```